Financial Planning Firm needs a client data collection summary sheet to print on A3

We are a financial advice company, and we are after a 1-page sheet where we can write all of the client’s personal information in our meetings, like a mind map.
It should have our logo on the page along with a place to put the Client's Name and the Date.
It also needs to have the following Headings
Family
Home
Investments
Business
Estate Plan
Lifestyle
Money
Retirement
Dreams & Goals
Health and Wellbeing
It also needs to have our License details on the bottom: Bellwood Counsel Pty Ltd (839162) is an Authorised Representative of Corrin Heritage Capital Group Pty Ltd AFSL No: 617058 ABN 72 915 483 206. This document has been prepared by Bellwood Counsel and is for general information only.
Please utilise our colour scheme as per our logo attached. Please find uploaded to the project an example data collection summary sheet that we use currently.

```html
<!DOCTYPE html>
<html lang="en">
<head>
<meta charset="utf-8">
<title>Bellwood Counsel – Personal Information Form</title>
<link href="https://fonts.googleapis.com/css2?family=Cinzel:wght@500&family=Montserrat:wght@500&family=PT+Sans+Narrow:wght@400;700&display=swap" rel="stylesheet">
<style>
  :root{
    --backdrop:#e8e8e6;
    --paper:#ffffff;
    --ink:#1a1a1a;
    --rule:#2b2b2b;
    --gold:#c9a36b;
    --bar-dark:#0d0d0d;
    --bar-mid:#6a6a6a;
  }
  *{box-sizing:border-box;margin:0;padding:0}
  html,body{width:1200px;height:784px;overflow:hidden}
  body{background:var(--backdrop);position:relative;font-family:"PT Sans Narrow",sans-serif;color:var(--ink)}

  .sheet{position:absolute;left:335px;top:17px;width:530px;height:750px;background:var(--paper);
    box-shadow:0 2px 10px rgba(0,0,0,.12);overflow:hidden}

  .corner{position:absolute;width:7px;height:46px;background:var(--gold)}
  .corner.tl{left:0;top:0;clip-path:polygon(0 0,100% 0,100% 70%,0 100%)}
  .corner.tr{right:0;top:0;clip-path:polygon(0 0,100% 0,100% 100%,0 70%)}
  .corner.bl{left:0;bottom:0;clip-path:polygon(0 0,100% 30%,100% 100%,0 100%)}
  .corner.br{right:0;bottom:0;clip-path:polygon(0 30%,100% 0,100% 100%,0 100%)}

  .brand{position:absolute;left:140px;right:14px;top:20px;height:30px;display:flex;align-items:center;justify-content:center;gap:10px;white-space:nowrap}
  .brand-mark{flex:none;width:10px;height:10px;background:var(--gold)}
  .brand-name{font-family:"Cinzel",serif;font-weight:500;font-size:23px;line-height:30px;letter-spacing:2px;color:var(--ink);white-space:nowrap}
  .form-title{position:absolute;left:140px;right:14px;top:56px;text-align:center;white-space:nowrap;
    font-family:"Montserrat",sans-serif;font-size:7px;letter-spacing:3.5px;color:var(--ink)}

  .field-label{position:absolute;font-size:10px;line-height:16px;color:var(--ink)}
  .name-label{left:16px;top:78px}
  .name-box{position:absolute;left:46px;top:78px;width:300px;height:16px;border:1px solid var(--rule)}
  .date-label{left:364px;top:78px}
  .date-boxes{position:absolute;left:402px;top:78px;display:flex}
  .date-boxes span{width:17px;height:16px;border:1px solid var(--rule);margin-left:-1px}

  .header-bar{position:absolute;left:58px;top:104px;width:430px;height:11px;
    background:linear-gradient(90deg,var(--bar-dark) 0%,var(--bar-mid) 75%,rgba(255,255,255,0) 100%);
    clip-path:polygon(0 0,100% 0,97% 100%,2% 100%)}

  .sections{position:absolute;left:14px;right:14px;top:128px;height:552px;display:flex;flex-direction:column}
  .section{position:relative;flex:1}
  .section-head{position:absolute;left:0;top:0;width:148px;height:18px;padding-left:8px;white-space:nowrap;
    background:linear-gradient(90deg,var(--bar-dark) 0%,var(--bar-dark) 45%,var(--bar-mid) 80%,#f2f2f2 100%);
    border-bottom:1.5px solid var(--gold);
    color:#fff;font-weight:700;font-size:11.5px;line-height:17px}
  .tick-box{position:absolute;left:156px;top:3px;width:13px;height:13px;border:1px solid var(--rule)}
  .head-rule{position:absolute;left:176px;right:0;top:17px;border-top:1px solid var(--rule)}
  .write-line{position:absolute;left:0;right:0;border-top:1px solid var(--rule)}
  .write-line.one{top:34px}
  .write-line.two{top:50px}

  .footer{position:absolute;left:24px;right:24px;bottom:18px;text-align:center}
  .footer-company{font-weight:700;font-size:9.5px;letter-spacing:.2px}
  .footer-dot{display:block;width:4px;height:4px;margin:2px auto 3px;background:var(--ink);border-radius:50%}
  .footer-licence{font-size:6.4px;line-height:1.3;color:#333}
</style>
</head>
<body>
  <main class="sheet">
    <div class="corner tl"></div>
    <div class="corner tr"></div>
    <div class="corner bl"></div>
    <div class="corner br"></div>

    <header>
      <div class="brand"><span class="brand-mark"></span><span class="brand-name">BELLWOOD COUNSEL</span></div>
      <div class="form-title">PERSONAL INFORMATION FORM</div>
      <span class="field-label name-label">Name</span>
      <div class="name-box"></div>
      <span class="field-label date-label">SOC Date</span>
      <div class="date-boxes"><span></span><span></span><span></span><span></span><span></span><span></span></div>
      <div class="header-bar"></div>
    </header>

    <section class="sections">
      <div class="section"><div class="section-head">Family</div><div class="tick-box"></div><div class="head-rule"></div><div class="write-line one"></div><div class="write-line two"></div></div>
      <div class="section"><div class="section-head">Home</div><div class="tick-box"></div><div class="head-rule"></div><div class="write-line one"></div><div class="write-line two"></div></div>
      <div class="section"><div class="section-head">Investments</div><div class="tick-box"></div><div class="head-rule"></div><div class="write-line one"></div><div class="write-line two"></div></div>
      <div class="section"><div class="section-head">Business</div><div class="tick-box"></div><div class="head-rule"></div><div class="write-line one"></div><div class="write-line two"></div></div>
      <div class="section"><div class="section-head">Estate Plan</div><div class="tick-box"></div><div class="head-rule"></div><div class="write-line one"></div><div class="write-line two"></div></div>
      <div class="section"><div class="section-head">Lifestyle</div><div class="tick-box"></div><div class="head-rule"></div><div class="write-line one"></div><div class="write-line two"></div></div>
      <div class="section"><div class="section-head">Money</div><div class="tick-box"></div><div class="head-rule"></div><div class="write-line one"></div><div class="write-line two"></div></div>
      <div class="section"><div class="section-head">Retirement</div><div class="tick-box"></div><div class="head-rule"></div><div class="write-line one"></div><div class="write-line two"></div></div>
      <div class="section"><div class="section-head">Dreams &amp; Goals</div><div class="tick-box"></div><div class="head-rule"></div><div class="write-line one"></div><div class="write-line two"></div></div>
      <div class="section"><div class="section-head">Health and Wellbeing</div><div class="tick-box"></div><div class="head-rule"></div><div class="write-line one"></div><div class="write-line two"></div></div>
    </section>

    <footer class="footer">
      <div class="footer-company">Bellwood Counsel Pty Ltd</div>
      <span class="footer-dot"></span>
      <p class="footer-licence">(839162) is an Authorised Representative of Corrin Heritage Capital Group Pty Ltd AFSL No: 617058 ABN 72 915 483 206. This document has been prepared by Bellwood Counsel and is for general information only.</p>
    </footer>
  </main>
</body>
</html>
```